Wix website for a food and nutrition consultancy

Professional looking wix website design needed for a food and nutrition consulting service soon to be established in Australia.
Key services include nutrition research, food regulations compliance, in-house dietitian services, project management and food/nutrition advisory.

Target Market(s)

The market is B2B (ie business clients) particularly food manufacturers, food companies, corporate clients, restaurants (secondary), import/exporters etc.

Industry/Entity Type

Business Consultant

Logo Text

Bright Harvest Food & Nutrition Consulting

Number of Pages Required

4 page

Colors
f37022
ffc214
fbed22
03a68d
33a6d7

Requirements
Must have
• Needs to be modern and streamlined looking. An overall look that can be aligned with a logo and provide a strong brand image. Some pictures featuring a range of different food groups. A nice colour scheme...please use your creative insight to decide on which colours would work...I have picked a few but they are not must haves.
Nice to have
• More food pictures than people pictures please.
Should not have
• -

```html
<!DOCTYPE html>
<html lang="en">
<head>
<meta charset="utf-8">
<title>Bright Harvest Food &amp; Nutrition Consulting</title>
<link rel="stylesheet" href="https://fonts.googleapis.com/css2?family=Montserrat:wght@500;600;700&family=Roboto:wght@400;500&display=swap">
<style>
  :root {
    --teal: #03a68d;
    --orange: #f37022;
    --yellow: #fbed22;
    --blue: #33a6d7;
    --text: #3a3a3a;
    --light: #f7f7f7;
    --white: #ffffff;
  }
  * { margin: 0; padding: 0; box-sizing: border-box; }
  html, body { width: 717px; height: 1200px; overflow: hidden; background: var(--white); }
  body { position: relative; font-family: "Montserrat", Arial, sans-serif; color: var(--text); }

  .abs { position: absolute; }
  .photo { position: absolute; }

  /* Hero */
  .hero { left: 0; top: 0; width: 717px; height: 317px; overflow: hidden;
    background: radial-gradient(ellipse at 60% 45%, #a0684a 0%, #7a4a34 30%, #d9d4cc 55%, #5a5656 80%, #3f3c3c 100%); }
  .hero-photo { inset: 0; }
  .site-header { left: 0; top: 0; width: 717px; height: 64px; background: rgba(55,55,55,.62); }
  .brand { left: 94px; top: 20px; display: flex; align-items: center; gap: 6px; }
  .brand-mark { width: 16px; height: 16px; border-radius: 50%; background: var(--orange); }
  .brand-name { font-size: 11px; font-weight: 600; color: var(--blue); line-height: 12px; width: 110px; }
  .main-nav { left: 453px; top: 27px; display: flex; gap: 10px; font-size: 8.4px; font-weight: 500; color: var(--white); letter-spacing: .1px; }
  .main-nav .current { color: var(--yellow); }
  .hero-title { left: 0; top: 156px; width: 717px; text-align: center; color: var(--white);
    font-size: 29px; font-weight: 700; line-height: 32px; letter-spacing: .5px; }
  .arrow { width: 14px; height: 14px; }

  /* About */
  .about-photo { left: 94px; top: 344px; width: 184px; height: 121px;
    background: linear-gradient(120deg, #6d6a5e 0%, #e88a2a 40%, #f3a13c 60%, #7a5c3c 100%); }
  .section-title { font-size: 14px; font-weight: 700; color: var(--teal); letter-spacing: .2px; }
  .about-title { left: 292px; top: 340px; }
  .about-text { left: 292px; top: 369px; width: 330px; font-family: "Roboto", Arial, sans-serif;
    font-size: 7.9px; font-weight: 500; line-height: 11.9px; color: #444; }
  .btn { display: flex; align-items: center; justify-content: center; font-size: 7.4px; font-weight: 600; letter-spacing: .3px; }
  .btn-teal { background: var(--teal); color: var(--white); }
  .btn-about { left: 292px; top: 445px; width: 61px; height: 20px; }

  /* Services */
  .services { left: 0; top: 492px; width: 717px; height: 274px; background: var(--light); }
  .services-title { left: 0; top: 516px; width: 717px; text-align: center; }
  .service-card { top: 547px; width: 168px; height: 154px; }
  .service-card .photo { left: 0; top: 0; width: 168px; height: 113px; }
  .service-label { position: absolute; left: 0; top: 113px; width: 168px; height: 41px; background: var(--orange);
    color: var(--white); font-size: 10.4px; font-weight: 600; line-height: 12px; text-align: center;
    display: flex; align-items: center; justify-content: center; }
  .btn-services { left: 328px; top: 719px; width: 61px; height: 20px; }

  /* Banner */
  .banner { left: 0; top: 766px; width: 717px; height: 168px;
    background: linear-gradient(100deg, #e6c04a 0%, #f0c84c 35%, #eeaa2e 65%, #e8b440 100%); }
  .banner-title { left: 0; top: 817px; width: 717px; text-align: center; color: var(--white);
    font-size: 27px; font-weight: 700; letter-spacing: .4px; }
  .btn-discover { left: 310px; top: 860px; width: 98px; height: 20px; background: var(--white); color: var(--teal); }

  /* Contact */
  .contact-title { left: 0; top: 958px; width: 717px; text-align: center; }
  .field { border-bottom: 1.5px solid var(--orange); font-family: "Roboto", Arial, sans-serif;
    font-size: 7.2px; color: var(--orange); padding-left: 9px; }
  .field-short { top: 989px; width: 165px; height: 13px; }
  .field-message { left: 100px; top: 1041px; width: 518px; height: 22px; }
  .btn-submit { left: 328px; top: 1082px; width: 61px; height: 20px; }

  /* Footer */
  .site-footer { left: 0; top: 1129px; width: 717px; height: 71px; background: var(--blue); }
  .footer-brand { left: 94px; top: 1153px; display: flex; align-items: center; gap: 5px; }
  .footer-mark { width: 10px; height: 10px; border-radius: 50%; background: var(--white); }
  .footer-name { color: var(--white); font-size: 7.6px; font-weight: 500; letter-spacing: .8px; }
  .copyright { left: 94px; top: 1179px; color: var(--white); font-size: 5.6px; font-weight: 500; }
  .social { top: 1153px; width: 25px; height: 23px; border: 1.2px solid var(--white); }
  .social-active { background: var(--yellow); border-color: var(--yellow); }
</style>
</head>
<body>

  <section class="abs hero">
    <div class="photo hero-photo" role="img" aria-label="Bowl of speckled borlotti beans with basil leaves and cherry tomatoes on a striped cloth"></div>
    <header class="abs site-header">
      <div class="abs brand">
        <span class="brand-mark"></span>
        <span class="brand-name">Bright Harvest Food &amp; Nutrition Consulting</span>
      </div>
      <nav class="abs main-nav">
        <span class="current">HOME</span><span>ABOUT US</span><span>SERVICES</span><span>CONTACT</span>
      </nav>
    </header>
    <h1 class="abs hero-title">HEALTY INSIDE<br>FRESH OUTSIDE</h1>
    <svg class="abs arrow" style="left:40px;top:183px" viewBox="0 0 14 14"><path d="M9 1 L3 7 L9 13" fill="none" stroke="#fff" stroke-width="2.2"/></svg>
    <svg class="abs arrow" style="left:663px;top:183px" viewBox="0 0 14 14"><path d="M5 1 L11 7 L5 13" fill="none" stroke="#fff" stroke-width="2.2"/></svg>
  </section>

  <section class="about">
    <div class="photo about-photo" role="img" aria-label="Glass of orange juice beside halved oranges on a wooden board"></div>
    <h2 class="abs section-title about-title">ABOUT US</h2>
    <p class="abs about-text">Lorem ipsum dolor sit amet, consectetur adipiscing elit. Nunc feugiat metus mi, in pellen-tesque tortor euismod in. Pellentesque pellentesque efficitur lacinia. Nunc condimentum turpis in lectus aliquet, at euismod diam consectetur. Aenean quis euismod sapien, eget maximus massa. Nulla quis viverra dui. Vestibulum a lacinia purus. Suspendisse a nulla quam. Integer sed molestie odio. Integer a ligula consequat, blandit sem at, egestas nunc.</p>
    <div class="abs btn btn-teal btn-about">MORE</div>
  </section>

  <section class="abs services"></section>
  <h2 class="abs section-title services-title">OUR SERVICES</h2>
  <svg class="abs arrow" style="left:40px;top:617px" viewBox="0 0 14 14"><path d="M9 2 L4 7 L9 12" fill="none" stroke="#33a6d7" stroke-width="2"/></svg>
  <svg class="abs arrow" style="left:663px;top:617px" viewBox="0 0 14 14"><path d="M5 2 L10 7 L5 12" fill="none" stroke="#33a6d7" stroke-width="2"/></svg>

  <article class="abs service-card" style="left:94px">
    <div class="photo" role="img" aria-label="Vegetables, notebook and laptop on a wooden desk" style="background:linear-gradient(135deg,#d8d4cc 0%,#8a5a3a 45%,#b8452c 70%,#e9e6e0 100%)"></div>
    <div class="service-label">Nutrition<br>Research</div>
  </article>
  <article class="abs service-card" style="left:275px">
    <div class="photo" role="img" aria-label="Salad bowl with alarm clock, tape measure and cutlery on wood" style="background:linear-gradient(120deg,#7d7262 0%,#c9c0ae 40%,#e0b33a 55%,#8a8070 100%)"></div>
    <div class="service-label">Food Regulations<br>Compliance</div>
  </article>
  <article class="abs service-card" style="left:455px">
    <div class="photo" role="img" aria-label="Notepad, tape measure and green salad on a wooden table" style="background:linear-gradient(120deg,#c2a582 0%,#e3e1d8 40%,#6e9a4a 70%,#b89872 100%)"></div>
    <div class="service-label">In-House Dietitian<br>Services</div>
  </article>
  <div class="abs btn btn-teal btn-services">MORE</div>

  <section class="abs banner" role="img" aria-label="Yellow-toned close-up of spaghetti, peppercorns and small oranges"></section>
  <h2 class="abs banner-title">FRESH ORGANIC FOOD</h2>
  <div class="abs btn btn-discover">DISCOVER MORE</div>

  <section class="contact">
    <h2 class="abs section-title contact-title">GET IN TOUCH</h2>
    <div class="abs field field-short" style="left:100px">Name</div>
    <div class="abs field field-short" style="left:277px">Email</div>
    <div class="abs field field-short" style="left:453px">Phone</div>
    <div class="abs field field-message">Message</div>
    <div class="abs btn btn-teal btn-submit">SUBMIT</div>
  </section>

  <footer class="abs site-footer"></footer>
  <div class="abs footer-brand">
    <span class="footer-mark"></span>
    <span class="footer-name">BRIGHT HARVEST</span>
  </div>
  <p class="abs copyright">© 2016 Bright Harvest Food &amp; Nutrition Consulting. All Rights Reserved</p>
  <div class="abs social" style="left:538px" aria-label="Social link"></div>
  <div class="abs social social-active" style="left:569px" aria-label="Social link"></div>
  <div class="abs social" style="left:598px" aria-label="Social link"></div>

</body>
</html>
```